Create modern and sleek business card for luxury real estate company

We're a "boutique" real estate office looking for a design that gets across a highly modern luxury brand. Blacks and whites are probably the best colors unless we try a silver foil for the logo. I've attached a version of our current logo here. I'd like to swap out the current font on there with Gotham Light Regular.

I'm looking to have one side of the card have the logo with the space for our agents info on the other side.

Target Market(s)

Young professionals in a "luxury" headspace

Industry/Entity Type

Real estate

Contact Information for Business Card

A place for agent name, cell number, website. The slogan "Simply Rethinking Real Estate".

Font styles to use
Other font styles liked:
• Gotham Regular

Colors

Designer to choose only greyscale colors for use in the design.

Requirements
Must have
• Matte black as the background color. Clean lines and use of contrast. A specific design aspect that will use silver foil.
Nice to have
• Up in the air on integrating a QR code
Should not have
• Any houses or other real estate related design (ex: a clip art house)

```html
<!DOCTYPE html>
<html lang="en">
<head>
<meta charset="utf-8">
<title>Halden Estates – Business Card</title>
<link href="https://fonts.googleapis.com/css2?family=Arimo:wght@400;700&family=Cinzel:wght@400&display=swap" rel="stylesheet">
<style>
  :root {
    --backdrop: #e6e6e4;
    --card-black: #232323;
    --card-edge: #1b1b1b;
    --foil: #ececec;
    --foil-soft: #cfcfcf;
    --emboss: #3a3a3a;
    --divider: #8a8a8a;
  }
  * { box-sizing: border-box; margin: 0; padding: 0; }
  html, body { width: 1200px; height: 801px; overflow: hidden; }
  body {
    background: var(--backdrop);
    font-family: "Arimo", Arial, sans-serif;
    position: relative;
  }
  .card {
    position: absolute;
    width: 520px;
    height: 297px;
    background: var(--card-black);
    border: 1px solid var(--card-edge);
    box-shadow: 0 10px 28px rgba(0,0,0,.22);
    color: var(--foil);
  }
  .card--front { left: 60px; top: 130px; }
  .card--back { left: 620px; top: 375px; overflow: hidden; }

  .brand {
    position: absolute;
    display: flex;
    align-items: center;
    gap: 14px;
  }
  .brand__circle {
    border: 2px solid var(--foil);
    border-radius: 50%;
    flex: none;
  }
  .brand__name {
    font-family: "Cinzel", Georgia, serif;
    font-weight: 400;
    color: var(--foil);
    line-height: 1.05;
    letter-spacing: .02em;
  }
  .card--front .brand { left: 120px; top: 40px; }
  .card--front .brand__circle { width: 62px; height: 62px; }
  .card--front .brand__name { font-size: 27px; }

  .agent {
    position: absolute;
    left: 70px; top: 150px;
    width: 190px;
    text-align: right;
  }
  .agent__name { font-weight: 700; font-size: 19px; }
  .agent__title { font-size: 13px; margin-top: 4px; color: var(--foil-soft); }

  .divider {
    position: absolute;
    left: 282px; top: 140px;
    width: 1px; height: 62px;
    background: var(--divider);
  }
  .contact {
    position: absolute;
    left: 300px; top: 140px;
    list-style: none;
    font-size: 13px;
  }
  .contact li { display: flex; align-items: center; gap: 8px; height: 21px; }
  .contact svg { width: 12px; height: 12px; flex: none; }

  .address {
    position: absolute;
    left: 0; right: 0; top: 240px;
    text-align: center;
    font-size: 13px;
    color: var(--foil-soft);
  }

  .backmark {
    position: absolute;
    left: 20px; top: 40px;
    width: 250px; height: 250px;
    border: 3px solid var(--emboss);
    border-radius: 50%;
  }
  .card--back .brand { left: 300px; top: 105px; }
  .card--back .brand__name { font-size: 38px; }
</style>
</head>
<body>

<section class="card card--front" aria-label="Card front with agent details">
  <div class="brand">
    <span class="brand__circle"></span>
    <div class="brand__name">Halden<br>Estates</div>
  </div>

  <div class="agent">
    <p class="agent__name">Daniel Hart</p>
    <p class="agent__title">Manager</p>
  </div>

  <span class="divider"></span>

  <ul class="contact">
    <li>
      <svg viewBox="0 0 24 24" aria-hidden="true"><path fill="currentColor" d="M6.6 10.8a15.1 15.1 0 0 0 6.6 6.6l2.2-2.2a1 1 0 0 1 1-.25 11.4 11.4 0 0 0 3.6.57 1 1 0 0 1 1 1V20a1 1 0 0 1-1 1A17 17 0 0 1 3 4a1 1 0 0 1 1-1h3.5a1 1 0 0 1 1 1c0 1.25.2 2.45.57 3.57a1 1 0 0 1-.25 1z"/></svg>
      555-014-2290
    </li>
    <li>
      <svg viewBox="0 0 24 24" aria-hidden="true"><rect x="3" y="5" width="18" height="14" rx="2" fill="none" stroke="currentColor" stroke-width="2"/><path d="M3 7l9 6 9-6" fill="none" stroke="currentColor" stroke-width="2"/></svg>
      daniel@haldenestates.com
    </li>
    <li>
      <svg viewBox="0 0 24 24" aria-hidden="true"><circle cx="12" cy="12" r="9" fill="none" stroke="currentColor" stroke-width="2"/><path d="M3 12h18M12 3c3 3 3 15 0 18M12 3c-3 3-3 15 0 18" fill="none" stroke="currentColor" stroke-width="1.6"/></svg>
      www.haldenestates.com
    </li>
  </ul>

  <p class="address">48 Linden Row, Ashford, CT 06278</p>
</section>

<section class="card card--back" aria-label="Card back with brand name">
  <span class="backmark"></span>
  <div class="brand">
    <div class="brand__name">Halden<br>Estates</div>
  </div>
</section>

</body>
</html>
```